Accounting Practice Business Card Design

I have a logo I am happy for you to use in the design of the Business Card.
You can edit and change colours as you please, I am not fixated on it.
I am looking for a modern and clean overall feel for the finished design.

The business is a small accounting practice who thrives on word of mouth referrals and this card will be given to all current and prospect clients.

Industry/Entity Type

Accountant

Contact Information for Business Card

Marcus Elwin
Level 5, 8 Corvale Ridge Road
ASHGROVE RISE VIC 3187
Phone: 9481 3057
Email: melwin@mrfaccountants.com.au
Web: www.mrfaccountants.com.au

Font styles to use
Serif
Sans Serif

Colors
0555a3
3277b5
85acd3
0393ce
33a6d7
85cae6
00a990
33b8a4
9bcb3c

Requirements
Must have
• "The end to your tax problems begin with us"
• "A referral from you is our greatest compliment"
Nice to have
• Modern clean professional

```html
<!DOCTYPE html>
<html lang="en">
<head>
<meta charset="utf-8">
<title>Corvale Accountants – Business Card</title>
<link href="https://fonts.googleapis.com/css2?family=Montserrat:wght@400;500;700;800&display=swap" rel="stylesheet">
<style>
  :root {
    --navy: #27406e;
    --green: #4a6a2a;
    --white: #ffffff;
    --backdrop: #2e2420;
    --card-shadow: rgba(0, 0, 0, 0.45);
  }
  html, body {
    margin: 0;
    width: 1200px;
    height: 1200px;
    overflow: hidden;
    background: var(--backdrop);
    font-family: "Montserrat", sans-serif;
  }
  .canvas {
    position: relative;
    width: 1200px;
    height: 1200px;
  }
  .card {
    position: absolute;
    left: 240px;
    width: 720px;
    height: 440px;
    background: var(--white);
    box-shadow: 0 18px 40px var(--card-shadow);
    overflow: hidden;
  }
  .card--front { top: 120px; }
  .card--back { top: 640px; }

  .brand {
    color: var(--navy);
    font-weight: 800;
    line-height: 1;
    text-transform: uppercase;
  }
  .brand__name { display: block; letter-spacing: 1px; }
  .brand__word { display: block; }

  /* Front */
  .card--front .brand {
    position: absolute;
    left: 44px;
    top: 62px;
    width: 226px;
  }
  .card--front .brand__name { font-size: 44px; }
  .card--front .brand__word { font-size: 20px; margin-top: 8px; letter-spacing: 4px; }

  .tagline-banner {
    position: absolute;
    left: 294px;
    top: 42px;
    width: 400px;
    height: 118px;
  }
  .tagline-banner svg { position: absolute; inset: 0; }
  .tagline-banner p {
    position: relative;
    margin: 0;
    padding: 20px 20px 0 22px;
    color: var(--white);
    font-size: 23px;
    font-weight: 500;
    line-height: 1.25;
  }

  .person-name {
    position: absolute;
    left: 62px;
    top: 222px;
    margin: 0;
    color: var(--navy);
    font-size: 26px;
    font-weight: 700;
  }
  .contact-list {
    position: absolute;
    left: 54px;
    top: 282px;
    margin: 0;
    padding: 0;
    list-style: none;
    color: var(--navy);
    font-size: 21px;
    line-height: 26px;
  }
  .contact-list li {
    display: flex;
    align-items: flex-start;
    gap: 14px;
  }
  .contact-list svg {
    flex: none;
    width: 18px;
    height: 18px;
    margin-top: 4px;
    fill: var(--green);
  }

  /* Back */
  .card--back .brand {
    position: absolute;
    left: 0;
    right: 0;
    top: 128px;
    text-align: center;
  }
  .card--back .brand__name { font-size: 66px; }
  .card--back .brand__word { font-size: 28px; margin-top: 10px; letter-spacing: 6px; }

  .referral-band {
    position: absolute;
    left: 0;
    right: 0;
    top: 306px;
    height: 92px;
    background: var(--navy);
    display: flex;
    align-items: center;
    justify-content: center;
  }
  .referral-band p {
    margin: 0;
    color: var(--white);
    font-size: 27px;
    font-weight: 500;
    line-height: 1.25;
    text-align: center;
    letter-spacing: 0.5px;
  }
</style>
</head>
<body>
<main class="canvas">

  <section class="card card--front" aria-label="Business card front">
    <div class="brand">
      <span class="brand__name">Corvale</span>
      <span class="brand__word">Accountants</span>
    </div>

    <div class="tagline-banner">
      <svg viewBox="0 0 400 118" width="400" height="118" aria-hidden="true">
        <path d="M0 0 H400 V10 C392 64 370 108 344 118 H0 Z" fill="var(--green)"/>
      </svg>
      <p>The end to your tax problems<br>begin with us.</p>
    </div>

    <h1 class="person-name">Marcus Elwin</h1>

    <ul class="contact-list">
      <li>
        <svg viewBox="0 0 24 24" aria-hidden="true"><path d="M12 1a8 8 0 0 0-8 8c0 6 8 14 8 14s8-8 8-14a8 8 0 0 0-8-8zm0 11a3 3 0 1 1 0-6 3 3 0 0 1 0 6z"/></svg>
        <span>Level 5, 8 Corvale Ridge Road<br>ASHGROVE RISE VIC 3187</span>
      </li>
      <li>
        <svg viewBox="0 0 24 24" aria-hidden="true"><path d="M6.6 10.8a15 15 0 0 0 6.6 6.6l2.2-2.2a1 1 0 0 1 1-.25 11.4 11.4 0 0 0 3.6.6 1 1 0 0 1 1 1V20a1 1 0 0 1-1 1A17 17 0 0 1 3 4a1 1 0 0 1 1-1h3.5a1 1 0 0 1 1 1c0 1.25.2 2.45.6 3.6a1 1 0 0 1-.25 1z"/></svg>
        <span>9481 3057</span>
      </li>
      <li>
        <svg viewBox="0 0 24 24" aria-hidden="true"><path d="M2 5h20v14H2zm2 2v.5l8 5 8-5V7l-8 5z"/></svg>
        <span>melwin@mrfaccountants.com.au</span>
      </li>
      <li>
        <svg viewBox="0 0 24 24" aria-hidden="true"><path d="M12 2a10 10 0 1 0 0 20 10 10 0 0 0 0-20zm-1 17.9A8 8 0 0 1 4.2 10L9 14.8v1a2 2 0 0 0 2 2zm6.9-2.5A2 2 0 0 0 16 16h-1v-3a1 1 0 0 0-1-1H8v-2h2a1 1 0 0 0 1-1V7h2a2 2 0 0 0 2-2v-.4a8 8 0 0 1 2.9 12.8z"/></svg>
        <span>mrfaccountants.com.au</span>
      </li>
    </ul>
  </section>

  <section class="card card--back" aria-label="Business card back">
    <div class="brand">
      <span class="brand__name">Corvale</span>
      <span class="brand__word">Accountants</span>
    </div>
    <div class="referral-band">
      <p>A referral from you is our<br>greatest compliment.</p>
    </div>
  </section>

</main>
</body>
</html>
```